"Landing Page Design for Premium Eco-Friendly Laundry Strips – Plooifris.nl"

We need a visually appealing and high-converting landing page for our premium laundry strips, emphasizing luxury, sustainability, and ease of use. The page should include sections such as:

Hero Section: A compelling introduction with a strong headline, subheadline, and a clear call-to-action (CTA).
Product Benefits: Highlighting key features like eco-friendliness, long-lasting scent, and hypoallergenic qualities.
Product Description: Focusing on innovation and sustainability.
How It Works: Simple, visual steps for using the product.
Customer Reviews: Authentic testimonials to build trust and social proof.
FAQ Section: Addressing common concerns about the product.
The design should maintain a luxurious aesthetic while ensuring clarity and user-friendliness. We also offer free shipping on all orders, a key differentiator to be prominently displayed. All texts and translations are already provided for implementation. Please deliver the design in Figma format."

Target Market(s)

"Eco-conscious consumers and families seeking premium and sustainable laundry solutions. Target age group: 25-50, predominantly women who prioritize luxury and environmental impact."

Industry/Entity Type

"Laundry care and eco-friendly consumer goods."

Coding

Requirements
Must have
• A visually luxurious design emphasizing premium quality and eco-friendliness. Clear call-to-actions (e.g., 'Try Now – Free Shipping'). Sections for product benefits, how it works, customer reviews, and FAQ. Highlight free shipping with no minimum order prominently."
Nice to have
• Elegant, minimalist animations to enhance the premium feel. Subtle use of gold and black to emphasize luxury, with a touch of green for sustainability. Interactive customer reviews section (e.g., carousel or testimonials)."
Should not have
• Overly cluttered designs or overwhelming text blocks. Generic stock photos not aligned with our brand identity. Bright or overly playful color schemes that detract from the premium feel."

```html
<!DOCTYPE html>
<html lang="nl">
<head>
<meta charset="utf-8">
<title>Plooifris Wasstrips</title>
<link href="https://fonts.googleapis.com/css2?family=Lexend:wght@300;400;500;600&family=Poppins:wght@400;500;600&display=swap" rel="stylesheet">
<style>
:root{
  --gold:#d4a537;
  --gold-light:#e8c25a;
  --gold-deep:#c0912a;
  --black:#0b0b0b;
  --ink:#1a1a1a;
  --grey:#555;
  --cream:#fbf4e6;
  --white:#fff;
}
*{margin:0;padding:0;box-sizing:border-box}
html,body{width:1200px;height:4922px;overflow:hidden}
body{font-family:"Poppins",sans-serif;color:var(--ink);background:var(--white);position:relative}
h1,h2,h3,.brand{font-family:"Lexend",sans-serif;font-weight:400}
section,header,footer{position:absolute;left:0;width:1200px;overflow:hidden}
.abs{position:absolute}
.btn{position:absolute;display:flex;align-items:center;justify-content:center;font-weight:600;font-size:16px;border-radius:3px;text-decoration:none}
.btn-gold{background:var(--gold);color:var(--white)}
.btn-black{background:var(--black);color:var(--white)}
.placeholder{position:absolute}

/* header + hero */
.hero{top:0;height:660px;background:radial-gradient(ellipse at 70% 40%,#2a2112 0%,var(--black) 55%)}
.brand{color:var(--gold);font-size:30px;letter-spacing:1px;display:flex;align-items:center;gap:12px}
.brand-dot{width:40px;height:40px;border:2px solid var(--gold);border-radius:50%}
.nav{top:32px;left:418px;display:flex;gap:0;color:var(--white);font-size:15px}
.nav span{padding:0 20px;border-left:1px solid #6b5a2e}
.nav span:first-child{border-left:none;padding-left:0}
.hero h1{left:130px;top:215px;font-size:52px;line-height:52px;color:var(--white)}
.hero h1 em{font-style:normal;color:var(--gold)}
.hero .lead{left:130px;top:390px;width:460px;font-size:16px;line-height:25px;color:var(--white)}
.hero .note{left:134px;top:530px;font-size:14px;color:#2e2a22}

/* benefits */
.benefits{top:630px;height:822px;background:var(--white)}
.section-title{position:absolute;left:0;width:1200px;text-align:center;font-size:32px;color:var(--ink)}
.benefit{position:absolute;width:300px}
.benefit h3{font-size:17px;font-weight:600;margin-bottom:4px;font-family:"Poppins",sans-serif}
.benefit p{font-size:15px;line-height:19px;color:#333}
.benefit.left{text-align:right;left:60px}
.benefit.right{left:850px}
.icon{position:absolute;width:50px;height:50px}
.rule{position:absolute;height:1px;background:#e6e0d2;width:290px}

/* product */
.product{top:1452px;height:608px;background:linear-gradient(100deg,#e9c565 0%,#d3a234 55%,#c38e25 100%)}
.product-title{position:absolute;left:669px;top:130px;font-size:40px;line-height:46px;color:var(--white)}
.product-bar{position:absolute;left:673px;top:230px;width:60px;height:3px;background:var(--white)}
.product-text{position:absolute;left:673px;top:256px;width:450px;font-size:17px;line-height:28px;color:var(--white)}

/* steps */
.steps{top:2060px;height:680px;background:radial-gradient(ellipse at 30% 20%,#231b0c 0%,var(--black) 60%)}
.step{position:absolute;top:214px;width:245px;height:287px;border:1px solid #3a301a;border-radius:22px;background:#0f0d09;text-align:center;color:var(--white);font-size:17px;line-height:21px}
.step .ring{width:144px;height:144px;border:2px solid var(--gold);border-radius:50%;margin:22px auto 0;position:relative;background:#0b0b0b;display:flex;align-items:center;justify-content:center}
.step .num{position:absolute;left:8px;bottom:-6px;width:30px;height:30px;border-radius:50%;background:var(--gold);color:var(--white);font-size:15px;font-weight:600;display:flex;align-items:center;justify-content:center}
.step p{margin-top:22px;padding:0 18px}

/* reviews */
.reviews{top:2715px;height:505px;background:var(--cream)}
.review{position:absolute;top:176px;height:210px;background:var(--white);outline:3px solid var(--white);border:2px solid #e5c467;text-align:center;padding-top:45px}
.stars{color:var(--gold);font-size:22px;letter-spacing:3px}
.review q{display:block;margin:10px auto 0;width:350px;font-size:15px;line-height:22px;color:#333}
.review .who{margin-top:12px;font-size:17px;color:#222}
.title-bar{position:absolute;left:570px;width:60px;height:3px;background:var(--gold)}

/* faq */
.faq{top:3220px;height:726px;background:var(--white)}
.faq-item{position:absolute;left:197px;width:800px;border:2px solid #f0d78c;background:var(--white)}
.faq-item h3{font-family:"Poppins",sans-serif;font-size:18px;font-weight:400;margin:32px 0 0 54px}
.faq-item p{font-size:15px;line-height:20px;margin:14px 0 0 56px;width:620px;color:#333}
.toggle{position:absolute;right:24px;width:26px;height:26px;border-radius:50%;background:var(--gold);color:var(--white);font-size:20px;line-height:25px;text-align:center}

/* closing cta */
.closing{top:3946px;height:640px;background:linear-gradient(100deg,#e7c35c 0%,#d8a93c 50%,#c6922a 100%)}
.closing h2{left:134px;top:158px;font-size:36px;line-height:45px;color:var(--white);position:absolute}

/* footer */
.footer{top:4548px;height:374px;background:var(--black);color:var(--white)}
.footer h4{font-family:"Lexend",sans-serif;font-weight:400;color:var(--gold);font-size:22px;margin-bottom:14px}
.footer .col{position:absolute;top:64px;font-size:15px;line-height:37px}
.footer .col h4{line-height:30px}
.social{display:flex;gap:10px;margin-top:14px}
.social span{width:34px;height:34px;border-radius:50%;background:var(--gold)}
.copyright{position:absolute;left:0;top:320px;width:1200px;text-align:center;font-size:13px;color:#999}
.divider{position:absolute;left:70px;top:296px;width:1060px;height:1px;background:#2a2a2a}
</style>
</head>
<body>

<header class="hero">
  <div class="brand abs" style="left:105px;top:26px"><span class="brand-dot"></span>PLOOIFRIS</div>
  <nav class="nav abs"><span>Voordelen</span><span>Product</span><span>Hoe het werkt</span><span>Beoordelingen</span><span>FAQ</span></nav>
  <a class="btn btn-black" style="left:990px;top:24px;width:128px;height:44px;font-size:15px;border:1px solid #222">Probeer nu</a>

  <h1 class="abs"><em>Ervaar Luxe en</em><br>Duurzaamheid in<br>Elke Wasbeurt</h1>
  <p class="lead abs">Ontdek de premium wasstrips van Plooifris – waar verfijning en ecologisch bewustzijn samenkomen</p>
  <a class="btn btn-gold" style="left:130px;top:462px;width:186px;height:46px">Probeer Nu ›</a>
  <p class="note abs">✓ Altijd Gratis Verzending</p>

  <div class="placeholder" role="img" aria-label="Verpakking Wasstrips in zwart en goud met witte golf" style="left:720px;top:120px;width:320px;height:480px;background:linear-gradient(160deg,#f4efe4 0%,#f4efe4 30%,#1a1710 31%,#0d0c08 100%);border-radius:4px"></div>
  <div class="placeholder" role="img" aria-label="Gouden lichtdeeltjes" style="left:620px;top:460px;width:560px;height:140px;background:radial-gradient(ellipse,rgba(212,165,55,.35),rgba(212,165,55,0) 70%)"></div>

  <svg class="abs" style="left:0;top:560px" width="1200" height="100" viewBox="0 0 1200 100">
    <path d="M0 60 Q300 40 600 65 T1200 0 L1200 100 L0 100Z" fill="var(--gold)"/>
    <path d="M0 80 Q300 55 620 78 T1200 30 L1200 100 L0 100Z" fill="var(--white)"/>
  </svg>
</header>

<section class="benefits">
  <h2 class="section-title" style="top:157px">Waarom Kiezen Voor Plooifris Wasstrips?</h2>

  <div class="placeholder" role="img" aria-label="Zwart-goud sierkader met bloemmotief" style="left:430px;top:258px;width:335px;height:470px;border-radius:48%/38%;background:radial-gradient(circle at 50% 45%,#6a5424 0%,#1b1710 45%,#0b0b0b 100%);box-shadow:0 0 0 6px #fff,0 0 0 8px #e3c470"></div>

  <div class="benefit left" style="top:283px"><h3>Milieuvriendelijk</h3><p>100% biologisch afbreekbaar<br>en plasticvrij.</p></div>
  <div class="benefit left" style="top:430px"><h3>Langdurige Geur</h3><p>Een heerlijke frisse geur die<br>dagenlang blijft hangen.</p></div>
  <div class="benefit left" style="top:609px"><h3>Geschikt voor Alle Stoffen</h3><p>Veilig voor fijne was, wit,<br>kleur en zwart.</p></div>
  <div class="rule" style="left:70px;top:378px"></div>
  <div class="rule" style="left:70px;top:548px"></div>
  <div class="rule" style="left:840px;top:378px"></div>
  <div class="rule" style="left:840px;top:548px"></div>

  <div class="benefit right" style="top:283px"><h3>Hypoallergeen</h3><p>Perfect voor de gevoelige<br>huid en babykleding.</p></div>
  <div class="benefit right" style="top:430px"><h3>Compact en<br>Gebruiksvriendelijk</h3><p>Geen gedoe met zware flessen –<br>scheur, voeg toe en geniet.</p></div>
  <div class="benefit right" style="top:609px"><h3>Altijd Gratis Verzending</h3><p>Geen minimale<br>bestelhoeveelheid vereist.</p></div>

  <svg class="icon" style="left:372px;top:290px" viewBox="0 0 50 50" fill="none" stroke="var(--gold)" stroke-width="2"><circle cx="25" cy="25" r="16"/><path d="M17 25l6 6 10-12"/></svg>
  <svg class="icon" style="left:372px;top:440px" viewBox="0 0 50 50" fill="none" stroke="var(--gold)" stroke-width="2"><path d="M15 40c-6-10 6-14 0-26M25 40c-6-10 6-14 0-26M35 40c-6-10 6-14 0-26"/></svg>
  <svg class="icon" style="left:372px;top:612px" viewBox="0 0 50 50" fill="none" stroke="var(--gold)" stroke-width="2"><rect x="12" y="18" width="26" height="22" rx="3"/><circle cx="25" cy="29" r="6"/></svg>
  <svg class="icon" style="left:778px;top:290px" viewBox="0 0 50 50" fill="none" stroke="var(--gold)" stroke-width="2"><path d="M10 16l8-6h14l8 6-5 6-3-2v20H18V20l-3 2z"/></svg>
  <svg class="icon" style="left:778px;top:440px" viewBox="0 0 50 50" fill="none" stroke="var(--gold)" stroke-width="2"><path d="M16 16c-5 8-5 14 0 16 5-2 5-8 0-16zM34 10c-6 10-6 18 0 20 6-2 6-10 0-20z"/></svg>
  <svg class="icon" style="left:778px;top:612px" viewBox="0 0 50 50" fill="none" stroke="var(--gold)" stroke-width="2"><rect x="6" y="16" width="24" height="18"/><path d="M30 22h8l6 7v5H30z"/><circle cx="14" cy="37" r="3"/><circle cx="37" cy="37" r="3"/></svg>
</section>

<section class="product">
  <div class="abs" style="left:109px;top:86px;width:480px;height:459px;border:2px solid #f3dc92;border-radius:70px 4px 70px 4px"></div>
  <div class="placeholder" role="img" aria-label="Verpakking Wasstrips op een zandkleurig voetstuk met zijden doek" style="left:120px;top:98px;width:460px;height:438px;border-radius:62px 0 62px 0;background:linear-gradient(150deg,#d7ccb9 0%,#b9ab93 45%,#efe6d6 100%)"></div>
  <h2 class="product-title">De Toekomst van<br>Wassen Is Hier</h2>
  <div class="product-bar"></div>
  <p class="product-text">Onze Plooifris Wasstrips combineren innovatie met duurzaamheid. Met slechts één strip per wasbeurt geniet je van een schone en heerlijk geurende was, zonder het milieu te belasten. Geen plastic flessen, geen verspilling – alleen pure waskracht in een handige strip.</p>
  <a class="btn btn-black" style="left:673px;top:446px;width:170px;height:46px">Probeer Nu ›</a>
</section>

<section class="steps">
  <h2 class="section-title" style="top:108px;color:var(--white);font-size:38px">Zo Gebruik Je Wasstrips</h2>

  <div class="step" style="left:80px"><div class="ring">
    <svg width="64" height="64" viewBox="0 0 64 64"><path d="M14 18l10-7h16l10 7-6 8-4-3v28H24V23l-4 3z" fill="var(--gold)"/></svg><span class="num">1</span></div>
    <p>Scheur een<br>wasstrip af</p></div>
  <div class="step" style="left:338px"><div class="ring">
    <svg width="64" height="64" viewBox="0 0 64 64" fill="none" stroke="var(--white)" stroke-width="2.5"><path d="M14 24h36l-4 28H18z"/><path d="M20 24c0-10 24-10 24 0"/><path d="M22 36h20M24 44h16"/></svg><span class="num">2</span></div>
    <p>Plaats de strip direct<br>in de trommel,<br>samen met je</p></div>
  <div class="step" style="left:597px"><div class="ring">
    <svg width="64" height="64" viewBox="0 0 64 64" fill="none" stroke="var(--white)" stroke-width="2.5"><rect x="14" y="10" width="36" height="44" rx="3"/><circle cx="32" cy="36" r="11"/><path d="M18 17h10"/></svg><span class="num">3</span></div>
    <p>Start de wasmachine<br>en laat de wasstrip<br>zijn werk doen.</p></div>
  <div class="step" style="left:855px"><div class="ring">
    <svg width="64" height="64" viewBox="0 0 64 64"><path d="M14 18l10-7h16l10 7-6 8-4-3v28H24V23l-4 3z" fill="var(--gold)"/></svg><span class="num">4</span></div>
    <p>Geniet van perfect<br>schone en fris<br>ruikende kleding!</p></div>

  <svg class="abs" style="left:306px;top:290px" width="640" height="40" viewBox="0 0 640 40" fill="none" stroke="var(--gold)" stroke-width="2" stroke-dasharray="4 5">
    <path d="M0 30 Q20 5 40 15"/><path d="M258 30 Q278 5 298 15"/><path d="M517 30 Q537 5 557 15"/>
  </svg>

  <a class="btn btn-gold" style="left:464px;top:543px;width:254px;height:48px;font-size:16px">Shop Nu – Vanaf €14,95 ›</a>

  <svg class="abs" style="left:0;top:600px" width="1200" height="80" viewBox="0 0 1200 80">
    <path d="M0 80 L0 55 Q500 40 1200 0 L1200 80Z" fill="var(--gold)"/>
    <path d="M0 80 L0 68 Q500 55 1200 18 L1200 80Z" fill="var(--cream)"/>
  </svg>
</section>

<section class="reviews">
  <h2 class="section-title" style="top:70px;font-size:38px">Wat Onze Klanten Zeggen</h2>
  <div class="title-bar" style="top:128px"></div>
  <svg class="abs" style="left:106px;top:250px" width="26" height="50" viewBox="0 0 26 50" fill="none" stroke="var(--gold)" stroke-width="3"><path d="M22 3L4 25l18 22"/></svg>
  <svg class="abs" style="left:1092px;top:250px" width="26" height="50" viewBox="0 0 26 50" fill="none" stroke="var(--gold)" stroke-width="3"><path d="M4 3l18 22L4 47"/></svg>

  <div class="review" style="left:188px;width:406px"><div class="stars">★★★★★</div>
    <q>Sinds ik Plooifris gebruik, voelt mijn was frisser en luxueuzer aan dan ooit.</q><div class="who">– Lotte</div></div>
  <div class="review" style="left:632px;width:400px"><div class="stars">★★★★★</div>
    <q>Eindelijk een milieuvriendelijk product dat echt werkt en heerlijk ruikt.</q><div class="who">– Daan</div></div>
</section>

<section class="faq">
  <h2 class="section-title" style="top:84px;font-size:38px">Heb Je Nog Vragen?</h2>

  <div class="faq-item" style="top:185px;height:161px">
    <h3>Zijn de wasstrips geschikt voor mensen met een gevoelige huid?</h3>
    <p>Ja, onze wasstrips zijn hypoallergeen en dermatologisch getest, waardoor ze veilig zijn voor de gevoelige huid.</p>
    <span class="toggle" style="top:26px">–</span>
  </div>
  <div class="faq-item" style="top:361px;height:73px">
    <h3 style="margin-top:22px">Hoeveel wasbeurten bevat één verpakking?</h3>
    <span class="toggle" style="top:24px">+</span>
  </div>
  <div class="faq-item" style="top:441px;height:75px">
    <h3 style="margin-top:22px">Werken de strips bij lage temperaturen?</h3>
    <span class="toggle" style="top:30px">+</span>
  </div>

  <a class="btn btn-gold" style="left:415px;top:566px;width:399px;height:59px;font-size:16px;background:#e6c35f">Bekijk Onze FAQ Voor Meer Antwoorden ›</a>
</section>

<section class="closing">
  <h2>Start Vandaag Met<br>Milieuvriendelijk Wassen<br>Geen Plastic, Geen Gedoe.<br>Alleen Fris Wassen</h2>
  <a class="btn btn-black" style="left:134px;top:363px;width:311px;height:52px;font-size:16px">Bestel Nu – Maak Het Verschil!</a>
  <div class="abs" style="left:626px;top:92px;width:444px;height:444px;border-radius:50%;background:var(--black)"></div>
  <div class="placeholder" role="img" aria-label="Wasmachine in een lichte ruimte met plant en de verpakking Wasstrips ervoor" style="left:640px;top:100px;width:426px;height:426px;border-radius:50%;background:radial-gradient(circle at 55% 40%,#f6f4ef 0%,#ddd8cf 60%,#b8b1a4 100%)"></div>
  <div class="placeholder" role="img" aria-label="Verpakking Wasstrips" style="left:690px;top:362px;width:132px;height:172px;background:linear-gradient(160deg,#f4efe4 0%,#f4efe4 28%,#15130d 29%,#0b0b0b 100%)"></div>
  <svg class="abs" style="left:0;top:540px" width="1200" height="100" viewBox="0 0 1200 100">
    <path d="M0 60 Q500 95 1200 20 L1200 100 L0 100Z" fill="var(--black)"/>
  </svg>
</section>

<footer class="footer">
  <div class="brand abs" style="left:124px;top:110px;font-size:28px">PLOOIFRIS</div>
  <div class="col" style="left:380px"><h4>Navigatie</h4>Voordelen<br>Product<br>Hoe het werkt</div>
  <div class="col" style="left:594px"><h4>Bronnen</h4>Beoordelingen<br>FAQ<br>Probeer het nu</div>
  <div class="col" style="left:820px"><h4>Contact opnemen</h4>
    <div style="display:flex;gap:12px;align-items:center;line-height:19px;font-size:14px">
      <svg width="34" height="34" viewBox="0 0 34 34"><circle cx="17" cy="17" r="17" fill="var(--gold)"/><rect x="9" y="11" width="16" height="12" fill="none" stroke="#111" stroke-width="1.8"/><path d="M9 11l8 7 8-7" fill="none" stroke="#111" stroke-width="1.8"/></svg>
      <span>Stuur ons een e-mail<br>info@plooifris.nl</span></div>
    <div class="social"><span></span><span></span><span></span><span></span></div>
  </div>
  <div class="divider"></div>
  <p class="copyright">Copyright © 2024 Wasstrips. Alle rechten voorbehouden.</p>
</footer>

</body>
</html>
```